New ideas for home page of my website

I am looking for some inspiration for my website www.crafthollowworks.com
Most of the content will stay the same but I will be adding on the following new buttons Annual Expo and Awards
Any ideas on alternative layout act will be great. The most creative idea will get the opportunity to pitch for the whole site design.

Colors

Designer to choose colors to be used in the design.

```html
<!DOCTYPE html>
<html lang="en">
<head>
<meta charset="utf-8">
<title>Craft Hollow Works – Home</title>
<link rel="stylesheet" href="https://fonts.googleapis.com/css2?family=Open+Sans:ital,wght@0,400;0,600;0,700;1,400&family=PT+Sans:wght@400;700&display=swap">
<style>
:root{
  --red:#d4131b;
  --red-dark:#b40e15;
  --ink:#222;
  --text:#555;
  --muted:#888;
  --header-bg:#f4f4f4;
  --nav-bg:#2b2b2b;
  --hero-a:#1d1d1d;
  --hero-b:#3a3a3a;
  --section-grey:#ececec;
  --card:#fff;
  --line:#d6d6d6;
  --badge:#c9d1da;
  --footer-bg:#f1f1f1;
}
*{box-sizing:border-box;margin:0;padding:0}
html,body{width:1200px;height:2448px;overflow:hidden}
body{position:relative;background:#fff;font-family:"Open Sans",Arial,sans-serif;color:var(--text)}
.abs{position:absolute}
h2,h3{font-family:"PT Sans",Arial,sans-serif}

/* header */
.site-header{left:0;top:0;width:1200px;height:136px;background:var(--header-bg)}
.brand{left:110px;top:28px;display:flex;align-items:center;gap:16px}
.brand-mark{width:80px;height:80px;border-radius:50%;background:var(--red)}
.brand-name{font-family:"PT Sans",sans-serif;font-weight:700;font-size:34px;line-height:36px;color:var(--red);width:230px}
.login{left:805px;top:33px;display:flex;gap:12px}
.login input{width:136px;height:32px;border:1px solid #c8c8c8;background:#fff;font:italic 14px "Open Sans",sans-serif;padding:0 10px;color:#777}
.forgot{left:866px;top:81px;font:italic 15px "Open Sans",sans-serif;color:#333;white-space:nowrap}
.btn-login{left:1034px;top:76px;width:54px;height:30px;background:var(--red);color:#fff;font-size:13px;line-height:30px;text-align:center}

/* nav */
.main-nav{left:0;top:136px;width:1200px;height:50px;background:var(--nav-bg)}
.main-nav ul{position:absolute;left:110px;top:0;display:flex;list-style:none}
.main-nav li{height:50px;line-height:50px;padding:0 16px;color:#ddd;font-size:15px;white-space:nowrap}
.main-nav li.active{background:var(--red);color:#fff}
.search{position:absolute;left:928px;top:12px;display:flex}
.search span{width:132px;height:28px;background:#fff;font-size:12px;line-height:28px;padding-left:10px;color:#777}
.search i{width:28px;height:28px;background:var(--red);display:block}

/* hero */
.hero{left:0;top:186px;width:1200px;height:550px;background:linear-gradient(90deg,var(--hero-a),var(--hero-b) 60%,#555)}
.hero h1{position:absolute;left:110px;top:150px;font-family:"PT Sans",sans-serif;font-weight:700;font-size:36px;line-height:48px;color:#fff;text-transform:uppercase}
.hero-ctas{position:absolute;left:110px;top:261px;display:flex}
.hero-ctas span{height:40px;line-height:40px;padding:0 16px;color:#fff;font-family:"PT Sans",sans-serif;font-size:20px;text-transform:uppercase}
.cta-primary{background:var(--red)}
.cta-secondary{background:#181818}
.hero-visual{position:absolute;left:717px;top:0;width:406px;height:550px;background:linear-gradient(160deg,#6a6a6a,#cfcfcf 45%,#e8d3c6 80%,#9a8f88)}
.hero-dots{position:absolute;left:112px;top:493px;width:86px;height:26px;background:var(--red);border-radius:3px;display:flex;justify-content:center;align-items:center;gap:8px}
.hero-dots b{width:9px;height:9px;border-radius:50%;background:#fff}

/* welcome */
.welcome{left:0;top:736px;width:1200px;height:180px;text-align:center}
.welcome h2{position:absolute;left:0;top:55px;width:1200px;font-weight:400;font-size:26px;color:#333}
.welcome .rule{position:absolute;top:74px;height:1px;width:250px;background:var(--line)}
.welcome p{position:absolute;left:0;top:105px;width:1200px;font-size:14px;color:var(--muted)}

/* content */
.content{left:0;top:916px;width:1200px;height:865px;background:var(--section-grey)}
.col-title{font-family:"PT Sans",sans-serif;font-weight:700;font-size:26px;color:var(--red);text-transform:uppercase;letter-spacing:.5px}
.card{background:var(--card);border:1px solid var(--line);box-shadow:0 1px 3px rgba(0,0,0,.12)}
.feature-img{left:14px;top:14px;width:342px;height:215px;background:linear-gradient(180deg,#a9b1b8,#cdd4d9)}
.feature h3{position:absolute;left:14px;top:258px;width:330px;font-size:21px;line-height:28px;color:#222}
.feature p{position:absolute;left:14px;top:362px;width:340px;font-size:15px;line-height:27px;color:#444}
.read-more{left:14px;top:622px;height:32px;line-height:32px;padding:0 12px;background:var(--red);color:#fff;font-size:15px}
.credit{left:14px;top:666px;font-size:14px;color:#444;white-space:nowrap}
.credit em{font-style:normal;color:var(--red)}
.pager{display:flex;gap:2px}
.pager i{width:16px;height:18px;background:#e6e6e6;border:1px solid #ccc;display:flex;align-items:center;justify-content:center}
.news-item{position:absolute;left:12px;width:226px;height:112px;border-bottom:1px solid #e5e5e5;padding-left:86px}
.news-thumb{position:absolute;left:0;top:0;width:72px;height:72px;background:linear-gradient(135deg,#9fa8b0,#e2e2e2)}
.news-item h4{font-weight:400;font-size:13px;line-height:18px;color:#333}
.news-item .by{margin-top:6px;font-size:12px;line-height:16px;color:#444}
.news-item .by b{color:var(--red);font-weight:600}
.member{position:absolute}
.event h3{position:absolute;left:14px;top:8px;font-size:21px;color:#222}
.event-logo{left:12px;top:45px;width:200px;height:82px;border:1px solid #e0e0e0;display:flex;align-items:center;justify-content:center;gap:8px}
.event-logo i{width:40px;height:40px;border-radius:50%;background:var(--red);display:block}
.event-logo span{font-family:"PT Sans",sans-serif;font-weight:700;font-size:17px;color:var(--red);width:110px;line-height:19px}
.event-title{left:236px;top:38px;font-family:"PT Sans",sans-serif;font-weight:700;font-size:22px;line-height:26px;color:var(--red)}
.event-meta{left:236px;top:96px;font-size:15px;line-height:20px;color:#333}
.btn-register{left:440px;top:120px;height:34px;line-height:34px;padding:0 12px;background:var(--red);color:#fff;font-size:15px}

/* partners */
.partners h2{position:absolute;left:110px;top:1826px;font-size:26px;letter-spacing:2px;color:#222;font-weight:700}
.badge{position:absolute;height:87px;background:var(--badge);border:1px solid #b6bfca}

/* footer */
.site-footer{left:0;top:2147px;width:1200px;height:260px;background:var(--footer-bg)}
.foot-title{position:absolute;font-family:"PT Sans",sans-serif;font-size:19px;color:var(--red)}
.foot-text{position:absolute;font-size:11px;line-height:17px;color:#333}
.foot-list{position:absolute;list-style:none;font-size:11px;line-height:20px;color:#333}
.foot-list li{display:flex;align-items:center;gap:6px}
.flag{width:14px;height:10px;display:inline-block}
.foot-brand{left:127px;display:flex;align-items:center;gap:8px}
.foot-brand i{width:50px;height:50px;border-radius:50%;background:var(--red);display:block}
.foot-brand span{font-family:"PT Sans",sans-serif;font-weight:700;font-size:20px;line-height:22px;color:var(--red);width:140px}
.newsletter{left:933px;top:2232px;display:flex}
.newsletter span{width:110px;height:26px;background:#fff;border:1px solid #ccc;font-size:11px;line-height:24px;padding-left:6px;color:#444}
.newsletter i{width:28px;height:26px;background:var(--red);display:block}
.bottom-bar{left:0;top:2407px;width:1200px;height:41px;background:var(--red);color:#fff;font-size:13px;line-height:41px}
</style>
</head>
<body>

<header class="site-header abs">
  <div class="brand abs"><span class="brand-mark"></span><span class="brand-name">Craft Hollow Works</span></div>
  <div class="login abs"><input value="Email Address"><input value="Password"></div>
  <span class="forgot abs">Forgotten password?</span>
  <span class="btn-login abs">Login</span>
</header>

<nav class="main-nav abs">
  <ul><li class="active">Home</li><li>Learn More</li><li>News</li><li>Events</li><li>Members</li><li>Council</li><li>Annual Expo</li><li>Awards</li></ul>
  <div class="search"><span>Enter your Search</span><i><svg width="28" height="28"><circle cx="13" cy="13" r="5" fill="none" stroke="#fff" stroke-width="2"/><line x1="17" y1="17" x2="21" y2="21" stroke="#fff" stroke-width="2"/></svg></i></div>
</nav>

<section class="hero abs">
  <h1>Championing world class<br>industry in the Midlands</h1>
  <div class="hero-ctas"><span class="cta-primary">Become a member</span><span class="cta-secondary">Learn more</span></div>
  <div class="hero-visual" role="img" aria-label="Photo of a hand holding a smartphone showing the website"></div>
  <div class="hero-dots"><b></b><b></b><b></b></div>
</section>

<section class="welcome abs">
  <span class="rule" style="left:150px"></span><span class="rule" style="left:800px"></span>
  <h2>Wellcome To Craft Hollow Works</h2>
  <p>Craft Hollow Works (CHW) exists to support and promote the interests of the manufacturing and engineering community in the Midlands.</p>
</section>

<section class="content abs"></section>

<h2 class="col-title abs" style="left:110px;top:956px">Featured Article</h2>
<h2 class="col-title abs" style="left:497px;top:956px">Latest News</h2>
<h2 class="col-title abs" style="left:767px;top:956px">Latest Members</h2>

<article class="card feature abs" style="left:110px;top:1021px;width:370px;height:698px">
  <div class="feature-img abs" role="img" aria-label="Illustration of a cloud with a question mark"></div>
  <h3>Product Lifecycle Management webinars demonstrate benefits to SMEs</h3>
  <p>Product Lifecycle Management (PLM) has been a 'must have' technology for largeAerospace and Automotive OEMs and their Tier 1 suppliers for almost thirtyyears. However in all that time, associated costs and complexity of theimplementation process has prevented SMEs from investing. Instead, critical operations are usually underpinned by a complex mix...</p>
  <span class="read-more abs">Read full article</span>
  <span class="credit abs">This article was courtesy of <em>Arclight Design</em></span>
  <div class="pager abs" style="left:318px;top:666px"><i><svg width="6" height="8"><path d="M5 0L0 4l5 4z" fill="#444"/></svg></i><i><svg width="6" height="8"><path d="M1 0l5 4-5 4z" fill="#444"/></svg></i></div>
</article>

<div class="card abs" style="left:497px;top:1021px;width:253px;height:511px">
  <div class="news-item" style="top:12px"><div class="news-thumb" role="img" aria-label="Website screenshot thumbnail"></div><h4>New Harbor StackFloor Website</h4><p class="by">By: <b>Harbor Forge Co. (Eastfield) Ltd</b></p></div>
  <div class="news-item" style="top:124px"><div class="news-thumb" role="img" aria-label="Gas spring product photo"></div><h4>TENSA gas springs from KESTREL PRESS UK</h4><p class="by">By: <b>Kestrel Press UK Ltd</b></p></div>
  <div class="news-item" style="top:236px"><div class="news-thumb" role="img" aria-label="Gas spring safety photo"></div><h4>TENSA gas springs safety &amp; reliability features</h4><p class="by">By: <b>Kestrel Press UK Ltd</b></p></div>
  <div class="news-item" style="top:348px;border:0"><div class="news-thumb" role="img" aria-label="Theatre sign photo"></div><h4>Ridgeway Powder Coating help revamp sign for local theatre</h4><p class="by">By: <b>Ridgeway Powder Coating</b></p></div>
  <div class="pager abs" style="left:196px;top:480px"><i><svg width="6" height="8"><path d="M5 0L0 4l5 4z" fill="#444"/></svg></i><i><svg width="6" height="8"><path d="M1 0l5 4-5 4z" fill="#444"/></svg></i></div>
</div>

<div class="card abs" style="left:767px;top:1021px;width:321px;height:511px">
  <span class="member" style="left:22px;top:22px;width:200px;height:64px;background:#e8731c"></span>
  <span class="member" style="left:22px;top:130px;width:190px;height:56px;background:#d52a22;border-radius:4px"></span>
  <span class="member" style="left:22px;top:234px;width:110px;height:104px;background:#4e5960"></span>
  <span class="member" style="left:175px;top:234px;width:115px;height:100px;background:#c8202c;border-radius:50%"></span>
  <span class="member" style="left:22px;top:375px;width:140px;height:100px;background:#e2381e"></span>
  <div class="pager abs" style="left:264px;top:470px"><i><svg width="6" height="8"><path d="M5 0L0 4l5 4z" fill="#444"/></svg></i><i><svg width="6" height="8"><path d="M1 0l5 4-5 4z" fill="#444"/></svg></i></div>
</div>

<div class="card event abs" style="left:497px;top:1558px;width:591px;height:165px">
  <h3>Upcoming Event</h3>
  <div class="event-logo abs"><i></i><span>Craft Hollow Works</span></div>
  <span class="event-title abs">Craft Hollow Works<br>2014 Exhibition</span>
  <span class="event-meta abs">Eastmoor Racecourse -<br>22/05/14, 09:00am</span>
  <span class="btn-register abs">Register Now</span>
</div>

<section class="partners">
  <h2>MAIN PARTNERS</h2>
  <span class="badge" style="left:110px;top:1895px;width:198px"></span>
  <span class="badge" style="left:325px;top:1895px;width:198px"></span>
  <span class="badge" style="left:545px;top:1895px;width:106px"></span>
  <span class="badge" style="left:674px;top:1895px;width:198px"></span>
  <span class="badge" style="left:889px;top:1895px;width:198px"></span>
  <span class="badge" style="left:110px;top:2001px;width:237px"></span>
  <span class="badge" style="left:370px;top:2001px;width:160px"></span>
  <span class="badge" style="left:553px;top:2001px;width:146px"></span>
  <span class="badge" style="left:717px;top:2001px;width:222px"></span>
</section>

<footer class="site-footer abs"></footer>
<span class="foot-title" style="left:127px;top:2178px">Registered Office</span>
<p class="foot-text" style="left:127px;top:2217px;width:210px">The birthplace of the industrial revolution and pioneers in advanced manufacturing</p>
<div class="foot-brand abs" style="top:2283px"><i></i><span>Craft Hollow Works</span></div>

<span class="foot-title" style="left:421px;top:2178px">Links</span>
<ul class="foot-list" style="left:421px;top:2220px"><li>Home</li><li>About Us</li><li>Learn more</li><li>News</li><li>Members</li><li>Lobbying</li></ul>
<ul class="foot-list" style="left:531px;top:2220px"><li>Team</li><li>Contact us</li><li>Blog</li><li>Terms and conditions</li></ul>

<span class="foot-title" style="left:693px;top:2178px">International</span>
<ul class="foot-list" style="left:693px;top:2220px">
  <li><i class="flag" style="background:linear-gradient(#c60b1e 25%,#ffc400 25% 75%,#c60b1e 75%)"></i>Espanol</li>
  <li><i class="flag" style="background:linear-gradient(90deg,#046a38 40%,#da291c 40%)"></i>Portugues</li>
  <li><i class="flag" style="background:linear-gradient(#000 33%,#dd0000 33% 66%,#ffce00 66%)"></i>Deutsch</li>
  <li><i class="flag" style="background:linear-gradient(90deg,#0055a4 33%,#fff 33% 66%,#ef4135 66%)"></i>Français</li>
  <li><i class="flag" style="background:linear-gradient(90deg,#009246 33%,#fff 33% 66%,#ce2b37 66%)"></i>Italiano</li>
  <li><i class="flag" style="background:#de2910"></i>日本語</li>
  <li><i class="flag" style="background:linear-gradient(#fff 50%,#dc143c 50%)"></i>Polska</li>
</ul>

<span class="foot-title" style="left:933px;top:2178px">News Letter</span>
<div class="newsletter abs"><span>Email to subscribe</span><i><svg width="28" height="26"><rect x="8" y="8" width="12" height="9" fill="none" stroke="#fff" stroke-width="1.5"/><path d="M8 8l6 5 6-5" fill="none" stroke="#fff" stroke-width="1.5"/></svg></i></div>

<div class="bottom-bar abs">
  <span class="abs" style="left:115px">Site Map &nbsp;|&nbsp; Terms and Conditions</span>
  <span class="abs" style="left:862px">Copyright © 2014 All rights Reserved</span>
</div>

</body>
</html>
```